Tidal Puffs. the aim is to sell vaping liquids based on mood or feelings

We are a company who sell vaping liquids. A designer from this site created a good logo for our company. I now need to use this logo and create a label to place onto vaping bottles. Unusually we will be selling vaping products based on Moods rather than flavours.

To be clear therefore the label should have our company Logo but then also reflect a particular type of Mood or feeling.

The designs for the various moods will then be printed as labels for our vaping bottles. We have 9 different Tidal Puffs (see below) that we intend to bring to the market and general public

i would therfore like designs for the following 9 feelings/moods:

Love
Chilled
Happy
Energy
Desire
Bliss
Lust
Calm
High

the first attachment has our stand alone Logo.

i will then send some attachments of ideas we were playing around with to point you in the right direction. i will need the designs to be very colourful and to reflect the mood.

i do like the love hart one so it doesn't necessarily mean that we need to have images of people on the label. i will leave it to the designers to use images they feel best reflects the specific mood

Target Market(s)

General public

Industry/Entity Type

Retail

Colors

Designer to choose colors to be used in the design.

Requirements
Must have
• my company logo on any design
Nice to have
• vibrant colours or image to match the particular mood vape

```html
<!DOCTYPE html>
<html lang="en">
<head>
<meta charset="utf-8">
<title>Tidal Puffs – Mood Labels</title>
<link href="https://fonts.googleapis.com/css2?family=Josefin+Sans:wght@200;400&display=swap" rel="stylesheet">
<style>
  :root {
    --canvas: #ffffff;
    --gold: #c9b77a;
    --gold-light: #e4d6a0;
    --night: #050505;
    --bliss: #5b7fd6;
    --calm: #9b5fd4;
    --chilled: #3fb3a2;
    --energy: #c8863a;
    --desire: #c9509e;
    --high: #3fb36a;
    --high-accent: #e46a9a;
    --happy: #b8a745;
    --love: #c9505a;
  }
  * { box-sizing: border-box; margin: 0; padding: 0; }
  html, body {
    width: 1200px;
    height: 603px;
    overflow: hidden;
    background: var(--canvas);
  }
  .label-sheet {
    width: 1200px;
    height: 603px;
    padding: 6px;
    display: grid;
    grid-template-columns: repeat(4, 291px);
    grid-template-rows: repeat(2, 291px);
    gap: 8px;
    font-family: "Josefin Sans", sans-serif;
  }
  .label {
    position: relative;
    border: 4px solid var(--gold);
    background: var(--night);
    overflow: hidden;
  }
  .label__smoke {
    position: absolute;
    inset: 0;
    background:
      radial-gradient(ellipse 70% 22% at 40% 72%, color-mix(in srgb, var(--tone) 70%, white) 0%, transparent 70%),
      radial-gradient(ellipse 80% 30% at 60% 38%, var(--tone) 0%, transparent 72%),
      radial-gradient(ellipse 90% 40% at 30% 60%, color-mix(in srgb, var(--tone) 55%, transparent) 0%, transparent 75%),
      var(--night);
    opacity: 0.9;
  }
  .label__brand {
    position: absolute;
    left: 14px;
    top: 26px;
    display: flex;
    align-items: center;
    gap: 6px;
    font-weight: 400;
    font-size: 14px;
    color: var(--gold-light);
    letter-spacing: 0.5px;
  }
  .label__brand-dot {
    width: 9px;
    height: 9px;
    border-radius: 50%;
    background: var(--gold-light);
  }
  .label__mood {
    position: absolute;
    left: 0;
    right: 0;
    top: 128px;
    text-align: center;
    font-weight: 200;
    font-size: 50px;
    line-height: 1;
    letter-spacing: 1px;
    color: var(--gold);
    text-transform: uppercase;
  }
  .label--bliss   { --tone: var(--bliss); }
  .label--calm    { --tone: var(--calm); }
  .label--chilled { --tone: var(--chilled); }
  .label--energy  { --tone: var(--energy); }
  .label--desire  { --tone: var(--desire); }
  .label--high    { --tone: var(--high); }
  .label--high .label__smoke {
    background:
      radial-gradient(ellipse 70% 22% at 40% 72%, var(--high-accent) 0%, transparent 70%),
      radial-gradient(ellipse 80% 30% at 60% 34%, var(--high) 0%, transparent 72%),
      var(--night);
  }
  .label--happy   { --tone: var(--happy); }
  .label--love    { --tone: var(--love); }
</style>
</head>
<body>
  <main class="label-sheet">
    <section class="label label--bliss">
      <div class="label__smoke" role="img" aria-label="Wisps of blue smoke on black"></div>
      <div class="label__brand"><span class="label__brand-dot"></span>Tidal Puffs</div>
      <h2 class="label__mood">Bliss</h2>
    </section>
    <section class="label label--calm">
      <div class="label__smoke" role="img" aria-label="Wisps of purple smoke on black"></div>
      <div class="label__brand"><span class="label__brand-dot"></span>Tidal Puffs</div>
      <h2 class="label__mood">Calm</h2>
    </section>
    <section class="label label--chilled">
      <div class="label__smoke" role="img" aria-label="Wisps of teal smoke on black"></div>
      <div class="label__brand"><span class="label__brand-dot"></span>Tidal Puffs</div>
      <h2 class="label__mood">Chilled</h2>
    </section>
    <section class="label label--energy">
      <div class="label__smoke" role="img" aria-label="Wisps of amber smoke on black"></div>
      <div class="label__brand"><span class="label__brand-dot"></span>Tidal Puffs</div>
      <h2 class="label__mood">Energy</h2>
    </section>
    <section class="label label--desire">
      <div class="label__smoke" role="img" aria-label="Wisps of magenta smoke on black"></div>
      <div class="label__brand"><span class="label__brand-dot"></span>Tidal Puffs</div>
      <h2 class="label__mood">Desire</h2>
    </section>
    <section class="label label--high">
      <div class="label__smoke" role="img" aria-label="Wisps of green and pink smoke on black"></div>
      <div class="label__brand"><span class="label__brand-dot"></span>Tidal Puffs</div>
      <h2 class="label__mood">High</h2>
    </section>
    <section class="label label--happy">
      <div class="label__smoke" role="img" aria-label="Wisps of golden yellow smoke on black"></div>
      <div class="label__brand"><span class="label__brand-dot"></span>Tidal Puffs</div>
      <h2 class="label__mood">Happy</h2>
    </section>
    <section class="label label--love">
      <div class="label__smoke" role="img" aria-label="Wisps of red smoke on black"></div>
      <div class="label__brand"><span class="label__brand-dot"></span>Tidal Puffs</div>
      <h2 class="label__mood">Love</h2>
    </section>
  </main>
</body>
</html>
```